Pellmont Creative Website

We need a website design for a UK based marketing and PR agency called "Pellmont Creative". We are a small and vibrant team that looks after a mixture of clients from the luxury lifestyle and professional services sectors so the design needs to reflect this and convey: Professionalism, contemporary approach, creativity and the high end luxury and professional market we look after. Our services include marketing, PR, social media and copywriting and we look after both local and national clients. The design will need to incorporate the grey and orange brand colours (logo attached) but we are open to the use of more/different colours - with the possibility of a slight refresh on the current logo/branding. The main pages required include: Home, About Us, Services, Sectors, Case Studies and Blog.

ur existing website can be seen here - http://www.pellmontcreative.co.uk

The site will need to showcase our approach, services and expertise, existing/previous clients, and provide frequently updated content via news and blog to support our marketing campaigns.

The key objectives for the site are:
- To support current sales activity by giving potential clients somewhere to visit to find out who we are, what we can do, what we have done
- To generate incoming sales leads/enquiries from companies looking for marketing and PR services
- To showcase us as a high end a professional agency with some fantastic clients and a wealth of experience

Target Market(s)

Professional services e.g. accountants, data centres etc
Luxury lifestyle e.g. wedding venue, tailor, homeware etc.
British market - mainly South East/London
Small - Medium sized businesses

Industry/Entity Type

Marketing

Font styles to use
Other font styles liked:
• Din Regular and Bold is currently used

Colors
f78f20
aaaaaa

Requirements
Must have
• Must Have:
- The main menu items are likely to be:
- Services
- Sectors
- About us
- Case Studies
- Blog
- Contact us

Some of these items may have a sub-menu, e.g. About us is likely to have "Company", "Team", and "Careers" below it and "Services" will have "marketing", "PR", "Copywriting", "Social media". Sectors will have "Professional", "Luxury", "Lifestyle"

Key must-have elements of the homepage include:
- Social media icons (twitter, linkedin, facebook, google+)
- Contact details (i.e. phone number and email/link)
- "We have worked with..." - this is likely to be icons for logos of previous and current clients
- "Sign up to newsletter"
- "Latest news"

Footer navigation must allow for the usual suspects (sitemap, t's & c's, privacy policy, company registration details)

Some kind of call-to-action boxes/areas/links to provide us with ways to link out to any specific micro-sites or pages within the site (e.g. to highlight some of our specific case studies, services etc).

To confirm, we are looking for the following page types/templates:
1) Home page
2) Inside/content page (can be used for services, about us etc)
3) Article page (for blog/news articles etc)
4) Case studies (an image led pad to showcase campaigns we have worked on)
4) Contact page
Nice to have
• - If web fonts are needed for the design, then please note we have an existing web fonts account with typevault.example and so can use any of the web fonts available there.
Should not have
• We do not want to use a one page-scroll down website

```html
<!DOCTYPE html>
<html lang="en">
<head>
<meta charset="utf-8">
<title>Pellmont Creative</title>
<link href="https://fonts.googleapis.com/css2?family=Montserrat:wght@500&family=Open+Sans:ital,wght@0,400;0,600;1,400&display=swap" rel="stylesheet">
<style>
:root{
  --orange:#f78f20;
  --dark:#2e2e30;
  --dark-active:#3b3b3d;
  --footer:#363638;
  --text:#333333;
  --muted:#8a8a8a;
  --icon-grey:#b3b3b3;
  --line:#e6e6e6;
  --white:#ffffff;
}
*{margin:0;padding:0;box-sizing:border-box}
html,body{width:800px;height:1200px;overflow:hidden;background:var(--white)}
body{position:relative;font-family:"Open Sans",Arial,sans-serif;color:var(--text)}
.abs{position:absolute}

/* header */
.site-header{left:0;top:0;width:800px;height:52px;background:var(--dark)}
.brand{left:106px;top:10px;color:var(--orange);font-size:16px;line-height:17px;font-weight:600}
.brand-mark{left:106px;top:12px;width:2px;height:32px;background:var(--icon-grey)}
.brand span{display:block;padding-left:6px}
.main-nav a{position:absolute;top:0;height:52px;line-height:52px;font-size:9px;color:#a9a9a9;text-decoration:none;transform:translateX(-50%)}
.main-nav a.active{color:var(--white);font-weight:600;background:var(--dark-active);width:66px;text-align:center}

/* hero */
.hero{left:0;top:52px;width:800px;height:324px;background:radial-gradient(ellipse at 70% 40%,#f4f2f0 0%,#dcdad8 45%,#c3c0bd 100%)}
.hero-title{left:105px;top:162px;font-family:"Montserrat",Arial,sans-serif;font-weight:500;font-size:27px;color:#1f1f1f}
.hero-text{left:106px;top:194px;width:350px;font-size:10px;line-height:12px;color:#222}

/* services */
.service{width:150px;text-align:center}
.service.active{background:var(--white);box-shadow:0 0 6px rgba(0,0,0,.15);height:181px}
.service-icon{position:absolute;left:50px;top:20px;width:50px;height:46px}
.service-icon i{position:absolute;left:0;top:0;width:3px;height:46px;background:var(--icon-grey)}
.service-icon b{position:absolute;left:4px;top:0;width:46px;height:46px;background:var(--icon-grey);display:flex;align-items:center;justify-content:center}
.service.active .service-icon b{background:var(--orange)}
.service h3{position:absolute;left:0;top:81px;width:150px;font-size:10px;font-weight:400;color:#222}
.service.active h3{color:var(--orange)}
.service p{position:absolute;left:4px;top:104px;width:142px;font-size:8px;line-height:14px;color:var(--muted)}

/* section headings */
.section-title{font-size:12px;font-weight:400;color:#222}
.arrows{width:22px;height:10px}
.arrows span{position:absolute;top:0;width:10px;height:10px;background:#cfcfcf}
.arrows span.next{left:11px;background:var(--orange)}

/* portfolio */
.work-tile{top:629px;width:146px;height:156px}
.work-overlay{display:flex;flex-direction:column;align-items:center;justify-content:center;color:var(--white);background:rgba(70,40,60,.45)}
.work-overlay .circle{width:30px;height:30px;border-radius:50%;background:var(--white);display:flex;align-items:center;justify-content:center;margin-bottom:10px}
.work-overlay h4{font-size:10px;font-weight:400}
.work-overlay small{font-size:7px}

/* blog */
.post{width:190px;height:130px}
.date-badge{position:absolute;left:0;top:0;width:30px;height:58px}
.date-badge .thumb{position:absolute;left:0;top:0;width:30px;height:30px;background:linear-gradient(#6f4a4a,#9a3a3a)}
.date-badge .date{position:absolute;left:0;top:30px;width:30px;height:28px;background:var(--orange);color:var(--white);text-align:center}
.date .m{display:block;font-size:6px;line-height:8px;padding-top:2px}
.date .d{display:block;font-size:14px;line-height:15px;font-weight:600}
.post h5{position:absolute;left:38px;top:-2px;font-size:8px;font-weight:600;color:#222}
.post .by{position:absolute;left:38px;top:11px;font-size:7px;color:#777}
.post .by b{color:#222}
.post p{position:absolute;left:38px;top:32px;width:140px;font-size:8px;line-height:14px;color:var(--muted)}
.post .more{position:absolute;left:38px;top:110px;font-size:8px;color:#222}
.post .more em{color:var(--orange);font-style:normal;margin-right:6px}

.quote{left:520px;top:865px;width:175px;height:112px;border:1px solid var(--line);padding:10px 10px;font-size:7.5px;line-height:13px;color:var(--muted)}
.author-photo{left:520px;top:984px;width:27px;height:27px;background:linear-gradient(#e0c9a8,#b89570)}
.author{left:551px;top:991px;font-size:8px;font-weight:600;color:#222}
.author small{font-weight:400;font-size:6.5px;color:#999;margin-left:2px}

/* footer */
.site-footer{left:0;top:1046px;width:800px;height:154px;background:var(--footer)}
.footer-title{font-size:12px;color:#e5e5e5;font-weight:400}
.footer-about{left:106px;top:1090px;width:380px;font-size:7px;line-height:13.5px;font-style:italic;color:#9a9a9a}
.footer-more{left:106px;top:1145px;font-size:8px;color:#e5e5e5;font-weight:600}
.copyright{left:106px;top:1173px;font-size:7.5px;color:#9a9a9a}
.contact-line{left:508px;font-size:7.5px;line-height:14px;color:#d0d0d0;font-weight:600}
.contact-line svg{position:absolute;left:0;top:3px}
.contact-line span{display:block;padding-left:11px}
.contact-line span.sub{font-weight:400}
</style>
</head>
<body>

<header class="site-header abs">
  <div class="brand-mark abs"></div>
  <div class="brand abs"><span>Pellmont</span><span>Creative</span></div>
  <nav class="main-nav">
    <a class="active" href="#" style="left:339px">Home</a>
    <a href="#" style="left:404px">About Us</a>
    <a href="#" style="left:473px">Services</a>
    <a href="#" style="left:539px">Sectors</a>
    <a href="#" style="left:613px">Case Studies</a>
    <a href="#" style="left:682px">Blog</a>
  </nav>
</header>

<section class="hero abs" role="img" aria-label="Photo of an elegant event table with wine glasses, white napkins, plated food and pink and white flowers"></section>
<h1 class="hero-title abs">Make Your Events Amazing</h1>
<p class="hero-text abs">Etiam rhoncus. Maecenas tempus, tellus eget condimentum rhoncus, sem quam semper libero, sit amet adipiscing sem neque sed ipsum.</p>

<section class="services">
  <div class="service abs" style="left:98px;top:399px">
    <div class="service-icon"><i></i><b><svg width="24" height="20" viewBox="0 0 24 20"><g fill="#fff"><rect x="1" y="13" width="3" height="6"/><rect x="6" y="10" width="3" height="9"/><rect x="11" y="11" width="3" height="8"/><rect x="16" y="7" width="3" height="12"/></g><path d="M1 10 L7 5 L12 8 L21 2" stroke="#fff" stroke-width="1.6" fill="none"/><path d="M17 1 L22 1 L22 6" stroke="#fff" stroke-width="1.6" fill="none"/></svg></b></div>
    <h3>Marketing and PR</h3>
    <p>Phasellus vehicula justo eget diam posuere sollicitudin eu tincidunt nulla. Curabitur eleifend tempor.</p>
  </div>
  <div class="service active abs" style="left:250px;top:399px">
    <div class="service-icon"><i></i><b><svg width="24" height="20" viewBox="0 0 24 20"><ellipse cx="9" cy="8" rx="8" ry="6" fill="#fff"/><path d="M4 12 L2 17 L8 13Z" fill="#fff"/><ellipse cx="16" cy="12" rx="7" ry="5" fill="#fff" stroke="#f78f20" stroke-width="1.2"/><path d="M19 16 L22 19 L18 16.5Z" fill="#fff"/><circle cx="13" cy="12" r="1" fill="#f78f20"/><circle cx="16" cy="12" r="1" fill="#f78f20"/><circle cx="19" cy="12" r="1" fill="#f78f20"/></svg></b></div>
    <h3>Social Media</h3>
    <p>Phasellus vehicula justo eget diam posuere sollicitudin eu tincidunt nulla. Curabitur eleifend tempor.</p>
  </div>
  <div class="service abs" style="left:398px;top:399px">
    <div class="service-icon"><i></i><b><svg width="26" height="18" viewBox="0 0 26 18"><path d="M13 9 L2 2 L4 9 L2 16Z M13 9 L24 2 L22 9 L24 16Z" fill="#fff"/><rect x="11" y="6" width="4" height="6" fill="#fff"/></svg></b></div>
    <h3>Events</h3>
    <p>Phasellus vehicula justo eget diam posuere sollicitudin eu tincidunt nulla. Curabitur eleifend tempor.</p>
  </div>
  <div class="service abs" style="left:548px;top:399px">
    <div class="service-icon"><i></i><b><svg width="22" height="22" viewBox="0 0 22 22"><path d="M4 18 L6 12 L16 2 L20 6 L10 16Z" fill="#fff"/><path d="M4 18 L3 20 L5 19Z" fill="#fff"/></svg></b></div>
    <h3>Copywriting</h3>
    <p>Phasellus vehicula justo eget diam posuere sollicitudin eu tincidunt nulla. Curabitur eleifend tempor.</p>
  </div>
</section>

<h2 class="section-title abs" style="left:105px;top:598px">Check Our Recent Work</h2>
<div class="arrows abs" style="left:672px;top:600px">
  <span style="left:0"><svg width="10" height="10"><path d="M6 2 L3 5 L6 8" stroke="#fff" fill="none"/></svg></span>
  <span class="next"><svg width="10" height="10"><path d="M4 2 L7 5 L4 8" stroke="#fff" fill="none"/></svg></span>
</div>

<div class="work-tile abs" style="left:106px;background:linear-gradient(#d9d4cc,#8e8a86)" role="img" aria-label="Photo of visitors at an exhibition hall"></div>
<div class="work-tile abs" style="left:253px;background:linear-gradient(#7c5a6a,#4a3c4c)" role="img" aria-label="Photo of a decorated event venue with draped curtains"></div>
<div class="work-tile work-overlay abs" style="left:253px">
  <div class="circle"><svg width="12" height="12" viewBox="0 0 12 12"><path d="M7 2 L11 6 L7 10 L7 7.5 C4 7.5 2 8.5 1 10.5 C1.5 6.5 4 4.5 7 4.5Z" fill="#f78f20"/></svg></div>
  <h4>Ajax Style Portfolio Item</h4>
  <small>Event / PR</small>
</div>
<div class="work-tile abs" style="left:400px;background:linear-gradient(#9a9790,#5f5a55)" role="img" aria-label="Photo of a crowd at an outdoor street event"></div>
<div class="work-tile abs" style="left:547px;width:146px;background:linear-gradient(#9a9790,#5f5a55)" role="img" aria-label="Photo of a crowd at an outdoor street event"></div>

<h2 class="section-title abs" style="left:106px;top:833px">Latest Blog Posts</h2>
<article class="post abs" style="left:106px;top:864px">
  <div class="date-badge"><div class="thumb" role="img" aria-label="Blog post thumbnail"></div><div class="date"><span class="m">JUNE</span><span class="d">25</span></div></div>
  <h5>Image Blog Title Here</h5>
  <div class="by">By: <b>Marcus Hale</b></div>
  <p>Phasellus vehicula justo eget diam posuere sollicitudin eu tincid nulla. curabitur eleifend magna scele lore ipsum is only free text isque placerat vele phasellus just.</p>
  <div class="more"><em>&rarr;</em>Read Ahead</div>
</article>
<article class="post abs" style="left:313px;top:864px">
  <div class="date-badge"><div class="thumb" role="img" aria-label="Blog post thumbnail"></div><div class="date"><span class="m">JUNE</span><span class="d">25</span></div></div>
  <h5>Image Blog Title Here</h5>
  <div class="by">By: <b>Marcus Hale</b></div>
  <p>Phasellus vehicula justo eget diam posuere sollicitudin eu tincid nulla. curabitur eleifend magna scele lore ipsum is only free text isque placerat vele phasellus just.</p>
  <div class="more"><em>&rarr;</em>Read Ahead</div>
</article>

<h2 class="section-title abs" style="left:520px;top:833px">What They Say</h2>
<div class="arrows abs" style="left:674px;top:839px">
  <span style="left:0"><svg width="10" height="10"><path d="M6 2 L3 5 L6 8" stroke="#fff" fill="none"/></svg></span>
  <span class="next"><svg width="10" height="10"><path d="M4 2 L7 5 L4 8" stroke="#fff" fill="none"/></svg></span>
</div>
<blockquote class="quote abs">Phasellus vehicula justo eget diam posuere sollicitudin eu tincid curabitur eleifend magna scelerisque placerat vele phasellus just co sollicitudin eu tincid nulla hasellus vehicula justo eget diam posuere sollicitudin tincid nulla. curabitur tincid tincid nulla.</blockquote>
<div class="author-photo abs" role="img" aria-label="Portrait photo of the client"></div>
<div class="author abs">Daniel Orme<small>Studio Team</small></div>

<footer class="site-footer abs"></footer>
<h2 class="footer-title abs" style="left:106px;top:1067px">More About Us</h2>
<p class="footer-about abs">Nullam quis ante. Etiam sit amet orci eget eros faucibus tincidunt. Duis leo. Sed fringilla mauris sit amet nibh. Donec sodales sagittis magna. Sed consequat, leo eget bibendum sodales, augue velit cursus nunc, quis gravida magna mi a libero. Nam pretium turpis et arcu. Duis arcu tortor, suscipit eget, imperdiet nec, imperdiet iaculis, ipsum. Sed aliquam ultrices mauris. Integer ante arcu, accumsan a, consectetuer eget, posuere ut, mauris. Praesent adipiscing.</p>
<div class="footer-more abs">More &raquo;</div>
<div class="copyright abs">&copy; 2013 Pellmont.</div>

<h2 class="footer-title abs" style="left:508px;top:1067px">Contact Us</h2>
<div class="contact-line abs" style="top:1090px">
  <svg width="7" height="9" viewBox="0 0 7 9"><path d="M3.5 0 C1.5 0 0 1.5 0 3.3 C0 5.5 3.5 9 3.5 9 C3.5 9 7 5.5 7 3.3 C7 1.5 5.5 0 3.5 0Z" fill="#9a9a9a"/><circle cx="3.5" cy="3.3" r="1.2" fill="#363638"/></svg>
  <span>48 Halden Row, Suite 12,</span><span class="sub">Brookfield, GA 30000</span>
</div>
<div class="contact-line abs" style="top:1131px">
  <svg width="8" height="6" viewBox="0 0 8 6"><rect width="8" height="6" fill="#9a9a9a"/><path d="M0 0 L4 3.5 L8 0" stroke="#363638" fill="none"/></svg>
  <span>office@pellmontcreative.com</span>
</div>
<div class="contact-line abs" style="top:1158px">
  <svg width="7" height="8" viewBox="0 0 7 8"><path d="M1 0 L3 0 L3.5 2 L2.5 3 C3 4.3 3.8 5 5 5.5 L6 4.5 L7 5.5 L7 7.5 C3 8 0 5 0 1Z" fill="#9a9a9a"/></svg>
  <span>P: +1 555 010-2040</span><span>F: +1 555 010-2040</span>
</div>

</body>
</html>
```